The Christian Teacher Life-Cycle

Look at the Lifecyle of the Christian School.
Look at the Veloran logo.
I am looking for a Christian Teacher Lifecycle that represents the slides in the PP upload.
Our website is faithacademyguidance.org.
The design should include a summary design showing all four stages, and then four slides representing each of the stages as subsets of the summary design.
When a teacher is going through the Lifecycle, they are going on their Professional Learning Journey that takes 40 years to unfold.
All five should include a copyright 2026 Veloran on them.

```html
<!DOCTYPE html>
<html lang="en">
<head>
<meta charset="UTF-8">
<title>Christian Teacher Lifecycle</title>
<link rel="stylesheet" href="https://fonts.googleapis.com/css2?family=Montserrat:wght@400;500;600&family=Playfair+Display:wght@700&display=swap">
<style>
  :root {
    --navy: #1b2a5c;
    --brand-blue: #1b6fb5;
    --logo-blue: #1a77ab;
    --ink: #111111;
    --muted: #3a3a3a;
    --soft-grey: #7a7f88;
    --card-top: #dfe8f3;
    --card-bottom: #f7fafd;
    --card-edge: #d5dce6;
    --sky-top: #d9e7f6;
    --sky-mid: #f6f9fd;
  }
  html, body { margin: 0; padding: 0; overflow: hidden; }
  body { width: 1200px; height: 848px; }
  .canvas {
    position: relative;
    width: 1200px;
    height: 848px;
    overflow: hidden;
    background: radial-gradient(ellipse at 50% 30%, #ffffff 0%, var(--sky-mid) 45%, var(--sky-top) 100%);
    font-family: "Montserrat", sans-serif;
  }
  .title {
    position: absolute;
    top: 50px; left: 0; width: 100%;
    margin: 0;
    text-align: center;
    font-family: "Playfair Display", serif;
    font-weight: 700;
    font-size: 52px;
    line-height: 64px;
    color: var(--navy);
  }
  .scenery {
    position: absolute;
    border-radius: 45% 45% 12% 12%;
    opacity: 0.3;
  }
  .scenery--tree-left {
    left: 0; top: 354px; width: 92px; height: 150px;
    background: linear-gradient(180deg, #c3d2e4, #d6e1ee);
  }
  .scenery--tree-right {
    left: 1092px; top: 400px; width: 86px; height: 132px;
    background: linear-gradient(180deg, #a9bdd6, #c9d6e6);
  }
  .stage {
    position: absolute;
    top: 190px;
    width: 216px;
    height: 440px;
    border: 1px solid var(--card-edge);
    border-radius: 22px;
    background: linear-gradient(180deg, var(--card-top), var(--card-bottom) 60%);
    text-align: center;
  }
  .stage--1 { left: 114px; }
  .stage--2 { left: 357px; }
  .stage--3 { left: 600px; }
  .stage--4 { left: 843px; }
  .stage__number {
    position: absolute;
    top: -24px; left: 50%;
    transform: translateX(-50%);
    width: 50px; height: 50px;
    border-radius: 50%;
    background: var(--brand-blue);
    color: #fff;
    font-weight: 600;
    font-size: 21px;
    line-height: 50px;
  }
  .stage__heading {
    position: absolute;
    top: 45px; left: 8px; right: 8px;
    margin: 0;
    font-weight: 600;
    font-size: 17px;
    line-height: 20.5px;
    color: var(--ink);
  }
  .stage--1 .stage__heading { font-size: 19px; line-height: 24px; top: 46px; }
  .stage__divider {
    position: absolute;
    top: 176px; left: 50%;
    width: 72px; height: 2px;
    transform: translateX(-50%);
    background: linear-gradient(90deg, transparent, #7f9cc2, transparent);
  }
  .stage__years {
    position: absolute;
    top: 205px; left: 0; right: 0;
    margin: 0;
    font-size: 16px;
    color: var(--muted);
  }
  .stage__doves {
    position: absolute;
    top: 250px; left: 30px; right: 30px;
    height: 104px;
    border-radius: 50%;
    background: radial-gradient(ellipse at 50% 50%, rgba(27,111,181,0.35), rgba(140,150,165,0.12) 60%, transparent 75%);
  }
  .hills {
    position: absolute;
    left: 0; top: 0;
    width: 1200px; height: 848px;
  }
  .leaves {
    position: absolute;
    left: 0; top: 616px;
    width: 205px; height: 232px;
    background: radial-gradient(ellipse at 20% 80%, rgba(47,79,176,0.75), rgba(63,143,208,0.45) 45%, transparent 72%);
  }
  .brand {
    position: absolute;
    top: 728px; left: 400px;
    width: 400px;
    text-align: center;
  }
  .brand__name {
    margin: 0;
    font-weight: 500;
    font-size: 52px;
    line-height: 64px;
    color: var(--logo-blue);
    letter-spacing: 1px;
  }
  .brand__tagline {
    margin: 12px 0 0;
    font-size: 12px;
    color: var(--soft-grey);
  }
  .copyright {
    position: absolute;
    right: 48px; top: 806px;
    margin: 0;
    font-size: 13px;
    color: var(--soft-grey);
  }
</style>
</head>
<body>
<main class="canvas">
  <h1 class="title">Christian Teacher Lifecycle</h1>

  <div class="scenery scenery--tree-left" role="img" aria-label="Faint silhouette of a tree"></div>
  <div class="scenery scenery--tree-right" role="img" aria-label="Faint silhouette of a tree"></div>

  <section class="stage stage--1">
    <div class="stage__number">01</div>
    <h2 class="stage__heading">The focus<br>is on “I”</h2>
    <div class="stage__divider"></div>
    <p class="stage__years">0-5 years</p>
    <div class="stage__doves" role="img" aria-label="One blue dove carrying an olive branch"></div>
  </section>

  <section class="stage stage--2">
    <div class="stage__number">02</div>
    <h2 class="stage__heading">Becoming part of<br>the Christian<br>Professional<br>Learning<br>Community</h2>
    <div class="stage__divider"></div>
    <p class="stage__years">5-10 years</p>
    <div class="stage__doves" role="img" aria-label="One blue dove and two grey doves in flight"></div>
  </section>

  <section class="stage stage--3">
    <div class="stage__number">03</div>
    <h2 class="stage__heading">Learning<br>leadership within<br>the faculty culture<br>/ CPLC</h2>
    <div class="stage__divider"></div>
    <p class="stage__years">10-30 years</p>
    <div class="stage__doves" role="img" aria-label="Two grey doves following a blue dove"></div>
  </section>

  <section class="stage stage--4">
    <div class="stage__number">04</div>
    <h2 class="stage__heading">So good, I am<br>“invisible”; I have<br>let go of control<br>and share it with<br>my children/teens</h2>
    <div class="stage__divider"></div>
    <p class="stage__years">30-40 years</p>
    <div class="stage__doves" role="img" aria-label="Three blue doves flying together"></div>
  </section>

  <svg class="hills" viewBox="0 0 1200 848" aria-hidden="true">
    <defs>
      <linearGradient id="hillBack" x1="0" y1="0" x2="1" y2="0">
        <stop offset="0" stop-color="#7f9cc9"/>
        <stop offset="0.35" stop-color="#b9cde6"/>
        <stop offset="0.7" stop-color="#dfe7f2"/>
        <stop offset="1" stop-color="#8ea6cf"/>
      </linearGradient>
      <linearGradient id="hillFront" x1="0" y1="0" x2="0" y2="1">
        <stop offset="0" stop-color="#e1ebf7"/>
        <stop offset="1" stop-color="#f4f8fc"/>
      </linearGradient>
    </defs>
    <path d="M0 512 C80 505 160 540 220 575 C280 610 310 618 360 602 C430 580 520 600 620 615 C720 628 820 580 920 572 C1000 566 1040 580 1070 568 C1110 550 1160 530 1200 528 L1200 848 L0 848 Z" fill="url(#hillBack)"/>
    <path d="M0 600 C90 590 180 612 260 612 C340 612 420 590 520 600 C640 612 720 640 820 628 C920 616 1000 572 1080 576 C1140 580 1180 600 1200 610 L1200 848 L0 848 Z" fill="url(#hillFront)" opacity="0.92"/>
  </svg>

  <div class="leaves" role="img" aria-label="Blue olive leaves branching up from the corner"></div>

  <div class="brand">
    <p class="brand__name">Veloran</p>
    <p class="brand__tagline">mentoring · growth · renewal</p>
  </div>

  <p class="copyright">Copyright© 2026 Veloran</p>
</main>
</body>
</html>
```